Organic Soap Packaging

We need a package design for a new company called Willow Naturals. Our primary product is organic soap. Our business model is based on the social entrepreneurial concept of by one give one like Brend shoes. We are giving soap to help prevent the spread of disease; 1.4 million deaths a year can be prevented by hand washing.

The design is for a recycled cardboard box/package. We want to demonstrate the high end, luxury feel of the product with undertones of organic/earth friendly/social conscious.

The soap is small batch, spa like, essential oil scented all natural luxury.
Updates

I am very excited about this startup business and I believe we will have great success! I am passionate about organic personal care and helping others in need. If you share my passion, please bring your work to the table!

Target Market(s)

My target market is people who are educated through college. Health conscious, socially conscious, Generation X. Basically shoppers of Green Basket and Haverline.

Industry/Entity Type

Business

Requirements
Must have
• Suitable for Face, Hair, and Skin
Scented with Organic Essential Oils

```html
<!DOCTYPE html>
<html lang="en">
<head>
<meta charset="utf-8">
<title>Willow Naturals – Organic Soap Box Front</title>
<link rel="stylesheet" href="https://fonts.googleapis.com/css2?family=Sorts+Mill+Goudy&display=swap">
<style>
  :root {
    --backdrop: #ffffff;
    --box-tint: #e5eae3;
    --panel: #fefefe;
    --leaf-green: #8aa04a;
    --ink: #2b2b2b;
    --ornament-light: rgba(214, 224, 192, 0.75);
    --ornament-mid: rgba(190, 204, 158, 0.85);
    --ornament-fade: rgba(214, 224, 192, 0);
  }
  * { margin: 0; padding: 0; box-sizing: border-box; }
  html, body {
    width: 1200px;
    height: 1000px;
    overflow: hidden;
    background: var(--backdrop);
  }
  .canvas {
    position: relative;
    width: 1200px;
    height: 1000px;
    font-family: "Sorts Mill Goudy", "Goudy Old Style", Georgia, serif;
    color: var(--ink);
  }
  .box-front {
    position: absolute;
    left: 300px;
    top: 100px;
    width: 600px;
    height: 800px;
    background: var(--box-tint);
    overflow: hidden;
  }
  .label-panel {
    position: absolute;
    left: 62px;
    top: 56px;
    width: 500px;
    height: 640px;
    background: var(--panel);
    border-radius: 40px;
  }
  .brand-name {
    position: absolute;
    left: 0;
    right: 0;
    top: 150px;
    text-align: center;
    font-size: 58px;
    line-height: 1.1;
    color: var(--leaf-green);
    font-weight: 400;
  }
  .product-lines {
    position: absolute;
    left: 0;
    right: 0;
    top: 330px;
    text-align: center;
    font-size: 23px;
    line-height: 1.55;
  }
  .floral-ornament {
    position: absolute;
    left: 40px;
    top: 490px;
    width: 420px;
    height: 240px;
    background: radial-gradient(ellipse closest-side at 50% 50%,
      var(--ornament-mid) 0%,
      var(--ornament-light) 45%,
      var(--ornament-fade) 100%);
  }
  .usage-claim {
    position: absolute;
    left: 0;
    right: 0;
    bottom: 40px;
    text-align: center;
    font-size: 30px;
    letter-spacing: 0.2px;
  }
</style>
</head>
<body>
  <main class="canvas">
    <section class="box-front">
      <div class="label-panel">
        <h1 class="brand-name">Willow<br>Naturals</h1>
        <p class="product-lines">Organic Soap<br>Scented with Organic Essential Oils</p>
      </div>
      <div class="floral-ornament" role="img" aria-label="Pale green floral swirl ornament with leaves and circles"></div>
      <p class="usage-claim">Suitable for Face, Hair, and Skin</p>
    </section>
  </main>
</body>
</html>
```